Letterhead Design Project

We are looking for a simple letterhead design that reflects our core purpose. We help our clients gain clarity and focus but we are there to help them execute. The letterhead design would mainly be utilised for engagement letters and contracts.

Target Market(s)

The customers of our business are large corporate organisations.

Requirements
Must have
• The letterhead must have the company logo
The font used must tie in to the font used in the company logo

Must have the following business details
Address: Level 10, 27 Brimley Lane, Melbourne, Australia, 3000
Phone: +61 3 502 847 193
Fax: +61 3 9412 5037
Website: www.vorndex.com.au
Twiiter: @vorndex

```html
<!DOCTYPE html>
<html lang="en">
<head>
<meta charset="utf-8">
<title>Vorndex Letterhead</title>
<link rel="stylesheet" href="https://fonts.googleapis.com/css2?family=Arimo:wght@400&display=swap">
<style>
  :root {
    --brand-dark: #0b5aa6;
    --brand-light: #1a9ad8;
    --paper: #ffffff;
  }
  html, body {
    margin: 0;
    padding: 0;
    width: 955px;
    height: 1200px;
    overflow: hidden;
    background: var(--paper);
  }
  .letterhead {
    position: relative;
    width: 955px;
    height: 1200px;
    background: var(--paper);
    font-family: "Arimo", Arial, sans-serif;
  }
  .brand {
    position: absolute;
    left: 12px;
    top: 4px;
  }
  .brand-name {
    margin: 0;
    font-size: 80px;
    font-weight: 400;
    line-height: 1;
    color: var(--brand-dark);
    letter-spacing: 1px;
  }
  .header-rule {
    position: absolute;
    left: 209px;
    top: 107px;
    width: 686px;
    height: 5px;
    background: var(--brand-light);
  }
  .address {
    position: absolute;
    right: 51px;
    top: 117px;
    margin: 0;
    font-size: 18.5px;
    color: var(--brand-light);
    font-style: normal;
  }
  .contact {
    position: absolute;
    left: 650px;
    top: 1107px;
    margin: 0;
    padding: 0;
    list-style: none;
    font-size: 18.5px;
    line-height: 21.7px;
    color: var(--brand-light);
  }
</style>
</head>
<body>
  <div class="letterhead">
    <header>
      <div class="brand">
        <h1 class="brand-name">Vorndex</h1>
      </div>
      <div class="header-rule"></div>
      <address class="address">Level 10, 27 Brimley Lane, Melbourne, Australia, 3000</address>
    </header>
    <footer>
      <ul class="contact">
        <li>Phone: +61 3 502 847 193</li>
        <li>Fax: +61 3 9412 5037</li>
        <li>Website: www.vorndex.com.au</li>
        <li>Twiiter: @vorndex</li>
      </ul>
    </footer>
  </div>
</body>
</html>
```